Medical Staffing agency

I need a logo design that can stand along and become a brand. I'm not too particular of the design. Want something catchy and hopefully related to the Health field. Not important though. An example of what I'm looking for is the Steel Harbor Logo, or the Solvent Logo. Something that can become a brand without having to say the brand name. A bit about my company, I hire medical staff, and contract with other companies to provide anywhere from short term to long term employees. But that is expanding to more than just that.

Industry/Entity Type

Medical

Contact Information for Business Card

Meridel Rehab Services
Lucas Brenner, CEO
842 Pinecroft Ave
Suite 71
Ashford, CA 95318

```html
<!DOCTYPE html>
<html lang="en">
<head>
<meta charset="utf-8">
<title>Meridel Rehab Services – Business Card</title>
<link href="https://fonts.googleapis.com/css2?family=Exo+2:wght@400&family=EB+Garamond:wght@400;700&family=Arimo:wght@400&display=swap" rel="stylesheet">
<style>
  :root {
    --backdrop: #000000;
    --card: #ffffff;
    --band: #231f20;
    --brand-blue: #22347a;
    --brand-red: #c9252c;
    --ink: #111111;
  }
  * { box-sizing: border-box; margin: 0; padding: 0; }
  html, body {
    width: 1200px;
    height: 1100px;
    overflow: hidden;
    background: var(--backdrop);
  }
  .sheet {
    position: relative;
    width: 1200px;
    height: 1100px;
  }
  .card {
    position: absolute;
    top: 386px;
    width: 560px;
    height: 328px;
    background: var(--card);
    overflow: hidden;
  }
  .card--front { left: 28px; }
  .card--back { left: 612px; }

  /* Front */
  .brand-lockup {
    position: absolute;
    left: 0;
    right: 0;
    top: 118px;
    display: flex;
    align-items: center;
    justify-content: center;
    gap: 16px;
  }
  .brand-lockup__mark {
    width: 34px;
    height: 34px;
    background: var(--brand-red);
    flex: none;
  }
  .brand-lockup__name {
    font-family: "Exo 2", sans-serif;
    font-weight: 400;
    color: var(--brand-blue);
    font-size: 27px;
    line-height: 1.05;
    letter-spacing: 0.5px;
  }
  .brand-lockup__name span { display: block; }
  .brand-lockup__sub { font-size: 18px; text-align: right; letter-spacing: 0.3px; }

  /* Back */
  .card__band {
    position: absolute;
    left: 0;
    right: 0;
    bottom: 0;
    height: 98px;
    background: var(--band);
  }
  .back-brand {
    position: absolute;
    left: 64px;
    top: 112px;
    width: 140px;
    font-family: "Exo 2", sans-serif;
    font-weight: 400;
    font-size: 17px;
    line-height: 1.15;
    color: var(--brand-blue);
  }
  .contact {
    position: absolute;
    left: 246px;
    top: 104px;
    color: var(--ink);
  }
  .contact__role {
    font-family: "EB Garamond", serif;
    font-size: 17px;
    text-decoration: underline;
    line-height: 1;
  }
  .contact__name {
    font-family: "EB Garamond", serif;
    font-weight: 700;
    font-size: 19px;
    line-height: 1.1;
    margin-bottom: 6px;
  }
  .contact__address {
    font-family: "Arimo", sans-serif;
    font-size: 18px;
    line-height: 1.22;
    font-style: normal;
  }
</style>
</head>
<body>
  <main class="sheet">
    <section class="card card--front" aria-label="Business card front">
      <div class="brand-lockup">
        <div class="brand-lockup__mark"></div>
        <div class="brand-lockup__name">
          <span>MERIDEL REHAB</span>
          <span class="brand-lockup__sub">Services LLC</span>
        </div>
      </div>
    </section>

    <section class="card card--back" aria-label="Business card back">
      <div class="back-brand">Meridel Rehab Services</div>
      <div class="contact">
        <p class="contact__role">CEO</p>
        <p class="contact__name">Lucas Brenner</p>
        <address class="contact__address">
          842 Pinecroft Ave Suite 71 Ashford<br>
          CA 95318
        </address>
      </div>
      <div class="card__band"></div>
    </section>
  </main>
</body>
</html>
```